RTV Event Lead Generation eFlyer

We need a brochure that highlights our Experiential Marketing and Event Management services. Using our corporate branding, images and icons, great an engaging and dynamic sales tool for our company designed to find qualified new business leads.

I would like the eFlyer in PDF format to send to clients via email, but would also like a working file (.doc) so that I can change the copy if needed.

Note: This is the first in a series of flyers. I would also eventually like to have printed versions, but for now I'm only doing electronic. My company offers 3 services: 1. Business Development; 2. Marketing Communications (this is the flyer you are working on); 3. Keynotes, i.e. motivational speaking. I will be producing a flyer for each of those services. The branding will be similar but the messaging will have a focus on the specific service.

Project Deadline Extended
Reason: I'm using this first experience with Pixel Harbor as a test. I'm looking for an affordable solution for ongoing design work. I would like to see more options coming in so that I can not only choose a great flyer, but can also choose a long term designer.

Target Market(s)

Marketing and Advertising Agencies, Production Companies

Industry/Entity Type

Marketing

Colors
e667a6
5c5c5c

Requirements
Must have
• Would like it to be clear, simple and inspiring. I want them to call me to discuss a project.
Nice to have
• Can convert copy to info graphs, I would like it to be visual and easy for someone to scan and get the information quickly.
Should not have
• I don't want it to be copy heavy.

```html
<!DOCTYPE html>
<html lang="en">
<head>
<meta charset="utf-8">
<title>RTV Experiential Marketing &amp; Event Management eFlyer</title>
<link href="https://fonts.googleapis.com/css2?family=Archivo+Black&family=Montserrat:wght@500;600;700;800&display=swap" rel="stylesheet">
<style>
  :root {
    --pink: #d8166c;
    --pink-soft: #e667a6;
    --grey: #5c5c5c;
    --grey-light: #cfcfcf;
    --ink: #111111;
    --paper: #ffffff;
    --stage: #e6e6e6;
  }
  * { box-sizing: border-box; margin: 0; padding: 0; }
  html, body { width: 1200px; height: 800px; overflow: hidden; }
  body { background: var(--stage); font-family: "Montserrat", Arial, sans-serif; color: var(--ink); }

  .brochure { position: absolute; left: 30px; top: 30px; width: 1140px; height: 740px; background: var(--paper); overflow: hidden; box-shadow: 0 6px 24px rgba(0,0,0,.18); }
  .fold { position: absolute; top: 0; bottom: 0; width: 1px; background: rgba(0,0,0,.08); }
  .fold--one { left: 380px; } .fold--two { left: 760px; }

  .top-strip { position: absolute; left: 0; top: 0; width: 560px; height: 18px; background: var(--ink); }
  .headline-field { position: absolute; left: 0; top: 18px; width: 580px; height: 300px; background: linear-gradient(180deg, #c4c4c4, #dcdcdc); clip-path: polygon(0 0, 100% 0, 92% 100%, 0 100%); }
  .visual-scribble { position: absolute; left: 500px; top: 0; width: 260px; height: 310px; background: radial-gradient(circle at 60% 45%, #2a2a2a, #0c0c0c 60%, #6a6a6a); clip-path: polygon(12% 0, 100% 0, 100% 86%, 0 100%, 16% 60%); }
  .visual-tightrope { position: absolute; left: 760px; top: 0; width: 380px; height: 255px; background: linear-gradient(160deg, #f1f1f1, #c9c9c9); }

  .headline { position: absolute; left: 26px; top: 42px; font-family: "Archivo Black", Arial, sans-serif; font-size: 38px; line-height: 38px; color: var(--ink); letter-spacing: .5px; }
  .intro { position: absolute; left: 26px; top: 216px; font-size: 15px; font-weight: 500; line-height: 20px; color: var(--ink); }

  .impact-band { position: absolute; left: 0; top: 250px; width: 760px; height: 140px; }
  .impact-text { position: absolute; left: 22px; top: 322px; width: 740px; color: var(--paper); font-weight: 700; font-size: 15px; line-height: 20px; transform: rotate(-3.2deg); transform-origin: left top; }

  .service-list { position: absolute; list-style: none; }
  .service-list--left { left: 28px; top: 400px; }
  .service-list--middle { left: 410px; top: 355px; }
  .service-list li { display: flex; align-items: center; gap: 14px; height: 40px; font-weight: 700; font-size: 14px; }
  .service-list--middle li { height: 44px; }
  .service-icon { width: 28px; height: 28px; flex: none; }

  .challenge { position: absolute; left: 785px; top: 270px; width: 335px; font-size: 14px; font-weight: 500; line-height: 19px; }
  .strengths { position: absolute; left: 785px; top: 392px; width: 340px; display: grid; grid-template-columns: 1fr 1fr; row-gap: 22px; column-gap: 10px; list-style: none; }
  .strength { display: flex; align-items: center; gap: 10px; font-weight: 800; font-size: 13px; line-height: 15px; }
  .strength-badge { width: 40px; height: 40px; flex: none; border-radius: 50%; background: var(--pink); display: flex; align-items: center; justify-content: center; }
  .team-note { position: absolute; left: 785px; top: 600px; width: 335px; font-size: 13px; font-weight: 500; line-height: 18px; }
  .team-note strong { display: block; margin-top: 4px; color: var(--pink); font-size: 17px; font-weight: 700; }
</style>
</head>
<body>
<main class="brochure">
  <div class="top-strip"></div>
  <div class="headline-field"></div>
  <div class="visual-scribble" role="img" aria-label="Tangled black line scribble illustration"></div>
  <div class="visual-tightrope" role="img" aria-label="Photo of a businessman balancing on a tightrope against a pale grey sky"></div>
  <div class="fold fold--one"></div>
  <div class="fold fold--two"></div>

  <h1 class="headline">EXPERIENTIAL<br>MARKETING &amp;<br>EVENT MANAGEMENT<br>SERVICES:</h1>
  <p class="intro">Need to fill a gap in a hurry with no time to hire?<br>We can help!<br>We offer agencies white label services.</p>

  <svg class="impact-band" viewBox="0 0 760 140" aria-hidden="true">
    <path d="M0 58 Q380 40 760 10 L760 72 Q380 104 0 128 Z" fill="var(--pink)"/>
  </svg>
  <p class="impact-text">Our team plugs in, ramps up to quickly deliver critical solutions<br>that make a big impact on your business! Our services include :</p>

  <ul class="service-list service-list--left">
    <li><svg class="service-icon" viewBox="0 0 28 28"><circle cx="14" cy="12" r="7" fill="none" stroke="var(--pink)" stroke-width="2.5"/><rect x="11" y="20" width="6" height="5" fill="var(--pink)"/></svg>Ideation &amp; Concept Development</li>
    <li><svg class="service-icon" viewBox="0 0 28 28"><rect x="4" y="6" width="20" height="16" rx="2" fill="none" stroke="var(--pink)" stroke-width="2.5"/><path d="M8 18 L20 10" stroke="var(--pink)" stroke-width="2.5"/></svg>Strategic Planning</li>
    <li><svg class="service-icon" viewBox="0 0 28 28"><rect x="3" y="8" width="16" height="13" fill="none" stroke="var(--pink)" stroke-width="2.5"/><circle cx="19" cy="12" r="5" fill="none" stroke="var(--pink)" stroke-width="2.5"/><path d="M22 16 L26 21" stroke="var(--pink)" stroke-width="2.5"/></svg>Research &amp; Feasbility</li>
    <li><svg class="service-icon" viewBox="0 0 28 28"><rect x="6" y="4" width="16" height="20" rx="2" fill="none" stroke="var(--pink)" stroke-width="2.5"/><path d="M10 14 l3 3 l6 -6" fill="none" stroke="var(--pink)" stroke-width="2.5"/></svg>Event Creation &amp; Logistics</li>
    <li><svg class="service-icon" viewBox="0 0 28 28"><path d="M2 16 L9 10 L14 14 L19 10 L26 16 L18 22 L10 22 Z" fill="var(--pink)"/></svg>Venue, Permit and Supplier Negotiations</li>
    <li><svg class="service-icon" viewBox="0 0 28 28"><circle cx="8" cy="10" r="4" fill="var(--pink)"/><circle cx="20" cy="10" r="4" fill="var(--pink)"/><circle cx="14" cy="16" r="4" fill="var(--pink)"/><rect x="3" y="19" width="22" height="6" rx="3" fill="var(--pink)"/></svg>Registration Management</li>
    <li><svg class="service-icon" viewBox="0 0 28 28"><rect x="4" y="14" width="20" height="8" fill="var(--pink)"/><rect x="8" y="6" width="12" height="8" fill="none" stroke="var(--pink)" stroke-width="2.5"/></svg>Hospitality</li>
    <li><svg class="service-icon" viewBox="0 0 28 28"><path d="M6 4 V24 M3 4 V11 H9 V4" fill="none" stroke="var(--pink)" stroke-width="2.5"/><rect x="14" y="10" width="10" height="14" fill="var(--pink)"/></svg>Food &amp; Beverage</li>
  </ul>

  <ul class="service-list service-list--middle">
    <li><svg class="service-icon" viewBox="0 0 28 28"><path d="M4 6 H16 L22 14 L16 22 H4 Z" fill="var(--pink)"/></svg>Design &amp; Décor</li>
    <li><svg class="service-icon" viewBox="0 0 28 28"><path d="M2 14 H6 L8 8 L11 20 L13 14 H16" fill="none" stroke="var(--pink)" stroke-width="2"/><path d="M17 11 L25 6 V22 L17 17 Z" fill="var(--pink)"/></svg>AV Production, Lighting and Sound</li>
    <li><svg class="service-icon" viewBox="0 0 28 28"><rect x="3" y="14" width="22" height="10" fill="var(--pink)"/><circle cx="20" cy="8" r="5" fill="none" stroke="var(--pink)" stroke-width="2.5"/></svg>Full Production Services</li>
    <li><svg class="service-icon" viewBox="0 0 28 28"><circle cx="14" cy="10" r="6" fill="none" stroke="var(--pink)" stroke-width="2.5"/><path d="M4 24 Q14 14 24 24 Z" fill="var(--pink)"/></svg>Creative Services</li>
    <li><svg class="service-icon" viewBox="0 0 28 28"><circle cx="14" cy="8" r="4" fill="var(--pink)"/><path d="M14 12 V18 M4 24 H24 M8 18 H20" stroke="var(--pink)" stroke-width="2.5"/></svg>Technology Management</li>
    <li><svg class="service-icon" viewBox="0 0 28 28"><path d="M2 18 L24 6 L26 9 L8 22 Z M12 14 L8 6 L11 5 L18 11" fill="var(--pink)"/></svg>Travel Logistics</li>
    <li><svg class="service-icon" viewBox="0 0 28 28"><path d="M3 11 H8 L15 5 V23 L8 17 H3 Z" fill="var(--pink)"/><path d="M19 9 Q23 14 19 19 M22 6 Q28 14 22 22" fill="none" stroke="var(--pink)" stroke-width="2"/></svg>Speaker Management</li>
    <li><svg class="service-icon" viewBox="0 0 28 28"><circle cx="14" cy="8" r="5" fill="var(--pink)"/><path d="M14 13 V18 M6 22 L14 18 L22 22" fill="none" stroke="var(--pink)" stroke-width="2"/><circle cx="6" cy="23" r="2.5" fill="var(--pink)"/><circle cx="22" cy="23" r="2.5" fill="var(--pink)"/></svg>Delegate Management</li>
  </ul>

  <p class="challenge">Your challenge is unique which is why we offer custom solutions to suit your specific issue. We can help! Tap into our service for short or long term support. Our team is ready to jump in and make an impact on your business.</p>

  <ul class="strengths">
    <li class="strength"><span class="strength-badge"><svg width="22" height="22" viewBox="0 0 22 22"><circle cx="6" cy="7" r="3" fill="#fff"/><circle cx="16" cy="7" r="3" fill="#fff"/><rect x="2" y="12" width="18" height="7" rx="3" fill="#fff"/></svg></span>Senior<br>Leadership</li>
    <li class="strength"><span class="strength-badge"><svg width="22" height="22" viewBox="0 0 22 22"><path d="M1 11 Q11 2 21 11 Q11 20 1 11 Z" fill="#fff"/><circle cx="11" cy="11" r="3.5" fill="var(--pink)"/></svg></span>Modern<br>Perspective</li>
    <li class="strength"><span class="strength-badge"><svg width="22" height="22" viewBox="0 0 22 22"><circle cx="5" cy="6" r="3" fill="#fff"/><circle cx="17" cy="6" r="3" fill="#fff"/><path d="M2 20 V12 H20 V20 M8 12 L11 16 L14 12" fill="none" stroke="#fff" stroke-width="2"/></svg></span>Collaborative<br>Mindset</li>
    <li class="strength"><span class="strength-badge"><svg width="22" height="22" viewBox="0 0 22 22"><rect x="3" y="3" width="16" height="16" rx="2" fill="none" stroke="#fff" stroke-width="2"/><circle cx="11" cy="11" r="3.5" fill="#fff"/></svg></span>Practical<br>Tools</li>
    <li class="strength"><span class="strength-badge"><svg width="22" height="22" viewBox="0 0 22 22"><circle cx="11" cy="13" r="3" fill="#fff"/><path d="M4 20 L11 16 L18 20 M6 5 L9 8 M16 5 L13 8" fill="none" stroke="#fff" stroke-width="2"/></svg></span>Depth of<br>Perspective</li>
    <li class="strength"><span class="strength-badge"><svg width="22" height="22" viewBox="0 0 22 22"><circle cx="11" cy="11" r="8" fill="none" stroke="#fff" stroke-width="2"/><circle cx="11" cy="11" r="3" fill="#fff"/></svg></span>Goal<br>Oriented</li>
  </ul>

  <p class="team-note">The RTV team is composed of highly motivated experts who are 100% focused on flawless and impactful results for our clients!<strong>We are only happy when you are!</strong></p>
</main>
</body>
</html>
```